Business Card Velostra - Accounting firm

Hi my friend.
I'm coming back to you to see if it would be possible for you to make a modern and minimalist business card design.
In shades of blue like the great logo you offered me.
The ideal is a modern and aesthetic business card.
The goal is to give a professional effect to the first exchanges.
Renewal and innovation in the accounting world !!
I thank you !!
Good evening to you

Target Market(s)

Young, dynamic and sensitive to marketing

Industry/Entity Type

Finance And Accounting

Contact Information for Business Card

Company logo and name. Last name, First name, Phone number, email address, company address, website.

Font styles to use
Sans Serif

Requirements
Must have
• The ideal is a modern and aesthetic business card.

Mentions to include: Company logo and name. Last name, First name, Phone number, email address, company address, website.
Nice to have
• The goal is to give a professional effect to the first exchanges.
Should not have
• Simplistic or childish design

```html
<!DOCTYPE html>
<html lang="en">
<head>
<meta charset="utf-8">
<title>Velostra – Business Card</title>
<link rel="stylesheet" href="https://fonts.googleapis.com/css2?family=Poppins:wght@400;500;600;700&display=swap">
<style>
  :root{
    --bg:#e4e4e2;
    --navy:#14306f;
    --navy-deep:#0f2a66;
    --blue:#1e4fa8;
    --teal:#3cc9b4;
    --teal-2:#2ba6c9;
    --paper:#fbfbfb;
    --white:#ffffff;
  }
  *{box-sizing:border-box;margin:0;padding:0}
  html,body{width:1200px;height:675px;overflow:hidden}
  body{
    background:var(--bg);
    font-family:"Poppins",sans-serif;
    display:flex;align-items:center;justify-content:center;gap:40px;
  }
  .card{
    width:525px;height:300px;border-radius:18px;position:relative;overflow:hidden;
    box-shadow:0 10px 30px rgba(0,0,0,.15);
  }

  /* front */
  .card--front{background:var(--paper);color:var(--navy)}
  .brand{position:absolute;left:40px;top:42px}
  .brand__name{
    display:flex;align-items:center;gap:10px;
    font-weight:600;font-size:30px;line-height:1;color:var(--navy);
  }
  .brand__mark{width:16px;height:16px;background:var(--teal);border-radius:3px}
  .brand__tagline{
    margin-top:6px;margin-left:26px;
    font-size:8px;font-weight:500;letter-spacing:3.2px;color:var(--navy);
  }
  .holder{position:absolute;right:40px;top:150px;text-align:right}
  .holder__name{font-size:26px;font-weight:600;color:var(--teal);line-height:1}
  .holder__role{font-size:11px;font-weight:500;color:var(--navy);margin-top:2px}
  .divider{
    position:absolute;left:40px;right:40px;top:198px;height:2px;
    background:linear-gradient(90deg,var(--teal),var(--blue));
  }
  .contacts{position:absolute;top:216px;display:flex;flex-direction:column;gap:10px}
  .contacts--left{left:40px}
  .contacts--right{right:40px}
  .contact{display:flex;align-items:center;gap:8px;font-size:12px;font-weight:600;color:var(--navy)}
  .contact svg{width:13px;height:13px;flex:none}

  /* back */
  .card--back{
    background:linear-gradient(135deg,var(--blue) 0%,var(--navy-deep) 100%);
    display:flex;align-items:center;justify-content:center;
  }
  .brand--back{position:static;text-align:left}
  .brand--back .brand__name{color:var(--white);font-size:46px;gap:14px}
  .brand--back .brand__mark{width:24px;height:24px;border-radius:4px}
  .brand--back .brand__tagline{color:var(--white);font-size:11px;letter-spacing:5px;margin-left:40px;margin-top:8px}
</style>
</head>
<body>

  <section class="card card--front" aria-label="Business card front">
    <div class="brand">
      <div class="brand__name"><span class="brand__mark"></span>Velostra</div>
      <div class="brand__tagline">EXPERT-COMPTABLE</div>
    </div>

    <div class="holder">
      <div class="holder__name">NAME</div>
      <div class="holder__role">Designation</div>
    </div>

    <div class="divider"></div>

    <div class="contacts contacts--left">
      <div class="contact">
        <svg viewBox="0 0 24 24"><path d="M12 2a7 7 0 0 0-7 7c0 5 7 13 7 13s7-8 7-13a7 7 0 0 0-7-7zm0 9.5A2.5 2.5 0 1 1 12 6.5a2.5 2.5 0 0 1 0 5z" fill="#2ba6c9"/></svg>
        Address
      </div>
      <div class="contact">
        <svg viewBox="0 0 24 24"><path d="M6.6 10.8a15 15 0 0 0 6.6 6.6l2.2-2.2a1 1 0 0 1 1-.25 11.4 11.4 0 0 0 3.6.57 1 1 0 0 1 1 1V20a1 1 0 0 1-1 1A17 17 0 0 1 3 4a1 1 0 0 1 1-1h3.5a1 1 0 0 1 1 1c0 1.25.2 2.45.57 3.6a1 1 0 0 1-.25 1z" fill="#2ba6c9"/></svg>
        Phone number
      </div>
    </div>

    <div class="contacts contacts--right">
      <div class="contact">
        <svg viewBox="0 0 24 24"><rect x="2" y="5" width="20" height="14" rx="2" fill="#2ba6c9"/><path d="M3 6l9 7 9-7" stroke="#fff" stroke-width="1.6" fill="none"/></svg>
        E-mail
      </div>
      <div class="contact">
        <svg viewBox="0 0 24 24"><circle cx="12" cy="12" r="9" fill="none" stroke="#2ba6c9" stroke-width="2"/><path d="M3 12h18M12 3c3 3 3 15 0 18M12 3c-3 3-3 15 0 18" stroke="#2ba6c9" stroke-width="1.6" fill="none"/></svg>
        Website
      </div>
    </div>
  </section>

  <section class="card card--back" aria-label="Business card back">
    <div class="brand brand--back">
      <div class="brand__name"><span class="brand__mark"></span>Velostra</div>
      <div class="brand__tagline">EXPERT-COMPTABLE</div>
    </div>
  </section>

</body>
</html>
```